Sunny Paths and joy Business card

I have a logo, but will like a business card design. Is for a travel agency in Mexico. We focus in family experiences.

I will liek some thing different and unique, from the traditional business card, something to get remmeber for.

Business card information:

Leandro T. Ocampo
leandro@sunnypathsjoy.example

Alameda 482, 3 piso
Col. Tlalpizco
Mexico, D.F. 07320

office: (55) 5000-0142
mobile: (55) 9000-0187

www.sunnypathsjoy.example
@sunnypjoy
blog: sunnypathsandjoy.blogsite.example
facebook: SunnyPathsAndJoy

```html
<!DOCTYPE html>
<html lang="es">
<head>
<meta charset="utf-8">
<title>Sunny Paths and joy — Business card</title>
<link rel="stylesheet" href="https://fonts.googleapis.com/css2?family=Roboto+Condensed:wght@400;700&display=swap">
<style>
  :root {
    --sky: #0b71bd;
    --road: #ffffff;
    --asphalt: #231f20;
    --lane: #9d9d9d;
    --halo: #cfe5f4;
    --brand: #1c3f8c;
    --ink-light: #ffffff;
  }
  html, body {
    margin: 0;
    padding: 0;
    overflow: hidden;
    background: #ffffff;
  }
  .card {
    position: relative;
    width: 1200px;
    height: 667px;
    overflow: hidden;
    background: var(--sky);
    font-family: "Roboto Condensed", "Arial Narrow", sans-serif;
    color: var(--ink-light);
  }
  .card__scenery {
    position: absolute;
    inset: 0;
  }
  .brand {
    position: absolute;
    left: 0;
    top: 0;
  }
  .brand__mark {
    position: absolute;
    left: 150px;
    top: 70px;
    width: 160px;
    height: 160px;
    border-radius: 50%;
    background: var(--halo);
  }
  .brand__name {
    position: absolute;
    left: 28px;
    top: 300px;
    margin: 0;
    font-size: 44px;
    font-weight: 700;
    line-height: 1;
    color: var(--brand);
    white-space: nowrap;
  }
  .holder {
    position: absolute;
    left: 550px;
    top: 50px;
  }
  .holder__name {
    margin: 0;
    font-size: 46px;
    font-weight: 700;
    line-height: 1.05;
    text-transform: uppercase;
  }
  .holder__email {
    margin: 2px 0 0;
    font-size: 34px;
    font-weight: 400;
    line-height: 1.1;
  }
  .address,
  .contact {
    position: absolute;
    margin: 0;
    font-style: normal;
    font-size: 30px;
    line-height: 39.5px;
  }
  .address {
    left: 63px;
    top: 516px;
  }
  .contact {
    left: 568px;
    top: 397px;
    list-style: none;
    padding: 0;
  }
</style>
</head>
<body>
  <main class="card">
    <svg class="card__scenery" width="1200" height="667" viewBox="0 0 1200 667" aria-hidden="true">
      <path class="road" fill="var(--road)"
        d="M0 311 C 200 262, 360 232, 520 232 C 720 234, 960 300, 1200 362
           L 1200 415 C 1000 390, 800 356, 560 358 C 350 360, 150 395, 0 440 Z"/>
      <path class="road-edge" fill="var(--sky)"
        d="M980 378 C 1070 380, 1150 386, 1200 390 L 1200 415 C 1120 404, 1050 392, 980 378 Z"/>
      <path class="lane-line" fill="none" stroke="var(--lane)" stroke-width="5"
        stroke-dasharray="44 30"
        d="M505 290 C 700 292, 950 330, 1200 394"/>
      <path class="asphalt" fill="var(--asphalt)"
        d="M0 440 C 150 395, 350 360, 560 358 C 800 356, 1000 390, 1200 415 L 1200 667 L 0 667 Z"/>
    </svg>

    <div class="brand">
      <span class="brand__mark"></span>
      <p class="brand__name">Sunny Paths and joy</p>
    </div>

    <header class="holder">
      <h1 class="holder__name">Leandro T. Ocampo</h1>
      <p class="holder__email">leandro@sunnypathsjoy.example</p>
    </header>

    <ul class="contact">
      <li>office: (55) 5000-0142</li>
      <li>mobile: (55) 9000-0187</li>
      <li>www.sunnypathsjoy.example</li>
      <li>@sunnypjoy</li>
      <li>blog: sunnypathsandjoy.blogsite.example</li>
      <li>facebook: SunnyPathsAndJoy</li>
    </ul>

    <address class="address">
      Alameda 482<br>
      3 piso, Col. Tlalpizco<br>
      Mexico, D.F. 07320
    </address>
  </main>
</body>
</html>
```